Holiday Rental Company Flyer Design (DL not A5)

Note from PixelFolk Administration: The category sizing selected is A5, however the project requires DL sized artwork. Please refer to the DL template link below while the 'Special Requirements' are updated accordingly.

Project Brief:
We need a double sided DL flyer designed for an up market Holiday Rental Company that portrays a personalised approach to property management. These are to be used for letter box drops to homes we're specifically targeting so the design should be modern, complimentary colour palette, uncluttered & visually appealing.

Please Download the DL Template from Quillmark here: http://www.quillmark.com.au/qm/ns/propath/UploadResources.aspx?selectedTab=0?pfid=BFB&pf_id=BFB&xnav=easypath-upload-image#Templates

Target Market(s)

Wealthy Home Owners

Industry/Entity Type

It Company

Font styles to use
Other font styles liked:
• Avant Garde Extra Light & Demi

Colors
33b8a4

Requirements
Must have
• DL Flyer sizes (210mm width x 99mm width, plus 3mm bleed)
• Front: Logo, Main Image & Grab
• Back: Contact Details & Brief Description of our business
• Images: Ideally the main image should be the house with the pool but alternatively a lifestyle images could also be used.
Nice to have
• A creative designer!
Should not have
• Clutter & busy designs

```html
<!DOCTYPE html>
<html lang="en">
<head>
<meta charset="utf-8">
<title>Headland Retreats — Holiday Rental Management</title>
<link href="https://fonts.googleapis.com/css2?family=Didact+Gothic&display=swap" rel="stylesheet">
<style>
  :root {
    --teal: #00b294;
    --ink: #1c1c1c;
    --brand-box: #2b2a2b;
    --brand-text: #f2f2f2;
    --night-deep: #1a1650;
    --night-violet: #4b3f8c;
    --interior-warm: #e9c98a;
    --pool-blue: #2f6dff;
  }
  html, body {
    margin: 0;
    padding: 0;
    overflow: hidden;
  }
  body {
    width: 1200px;
    height: 900px;
  }
  .flyer-front {
    position: relative;
    width: 1200px;
    height: 900px;
    background: var(--teal);
    overflow: hidden;
    font-family: "Didact Gothic", "Century Gothic", sans-serif;
  }
  .hero-shape {
    position: absolute;
    inset: 0;
    width: 1200px;
    height: 900px;
  }
  .brand-box {
    position: absolute;
    left: 31px;
    top: 36px;
    width: 199px;
    height: 137px;
    background: var(--brand-box);
    display: flex;
    flex-direction: column;
    align-items: center;
    justify-content: center;
    color: var(--brand-text);
    font-size: 29px;
    line-height: 1.1;
    letter-spacing: 2px;
    text-transform: uppercase;
  }
  .tagline {
    position: absolute;
    left: 545px;
    top: 794px;
    margin: 0;
    font-size: 26px;
    font-weight: 400;
    color: var(--ink);
    letter-spacing: -0.3px;
  }
</style>
</head>
<body>
  <main class="flyer-front">
    <svg class="hero-shape" viewBox="0 0 1200 900" role="img"
         aria-label="Photograph: modern luxury holiday home at dusk with lit interior, glass pool fence and a glowing blue pool beside a white wall water feature">
      <defs>
        <linearGradient id="dusk" x1="0" y1="0" x2="1" y2="0">
          <stop offset="0" stop-color="var(--interior-warm)"/>
          <stop offset="0.35" stop-color="#6b5a5a"/>
          <stop offset="0.55" stop-color="var(--night-deep)"/>
          <stop offset="1" stop-color="var(--night-violet)"/>
        </linearGradient>
        <radialGradient id="pool-glow" cx="0.45" cy="0.82" r="0.35">
          <stop offset="0" stop-color="var(--pool-blue)" stop-opacity="0.85"/>
          <stop offset="1" stop-color="var(--pool-blue)" stop-opacity="0"/>
        </radialGradient>
      </defs>
      <path d="M0,330 C250,175 700,70 1200,62 L1200,420 C1000,600 720,760 150,795 L0,795 Z" fill="url(#dusk)"/>
      <path d="M0,330 C250,175 700,70 1200,62 L1200,420 C1000,600 720,760 150,795 L0,795 Z" fill="url(#pool-glow)"/>
    </svg>

    <div class="brand-box">
      <span>Headland</span>
      <span>Retreats</span>
    </div>

    <p class="tagline">Holiday Rental Management with a difference</p>
  </main>
</body>
</html>
```